New business stationairy

I need paper with header and footer and business cards.
I am a Ltd Company and my main field of expertise is QA/QC inspection in the Oil and Gas Industry. I will need all contact detail inserted and a footer with registration number and bank details etc

Industry/Entity Type

Business

```html
<!DOCTYPE html>
<html lang="en">
<head>
<meta charset="utf-8">
<title>Harwell Inspection Services Ltd. – Letterhead</title>
<link rel="stylesheet" href="https://fonts.googleapis.com/css2?family=PT+Sans:wght@700&family=Michroma&display=swap">
<style>
  :root {
    --backdrop: #e9eef0;
    --paper: #ffffff;
    --band-light: #d6fcfc;
    --band-teal: #00bdd9;
    --ink-teal: #00b4d4;
    --art-soft: #8fe0ec;
  }
  * { box-sizing: border-box; margin: 0; padding: 0; }
  html, body {
    width: 901px; height: 1200px; overflow: hidden;
    background: var(--backdrop);
  }
  .letterhead {
    position: absolute; left: 70px; top: 60px;
    width: 761px; height: 1080px;
    background: var(--paper);
    box-shadow: 0 6px 24px rgba(0,0,0,.25);
    overflow: hidden;
  }
  .header {
    position: absolute; left: 0; top: 0; width: 100%; height: 215px;
    background: var(--band-light);
  }
  .header-rule {
    position: absolute; left: 0; bottom: 0; width: 100%; height: 30px;
    background: var(--band-teal);
  }
  .figure-art {
    position: absolute; left: 18px; top: 30px; width: 90px; height: 155px;
    background: var(--band-teal);
    border-radius: 36px 36px 0 0;
  }
  .skyline-art {
    position: absolute; left: 405px; right: 20px; top: 80px; height: 105px;
    background: linear-gradient(to bottom, var(--art-soft), var(--band-teal));
  }
  .company-name {
    position: absolute; z-index: 1; left: 122px; top: 30px;
    font: 700 30px/1 "PT Sans", sans-serif;
    color: var(--ink-teal);
    white-space: nowrap;
  }
  .contact {
    position: absolute; z-index: 1; left: 122px; top: 76px; width: 270px;
    text-align: center;
    font: 700 15px/1.2 "PT Sans", sans-serif;
    font-style: normal;
    color: var(--ink-teal);
  }
  .contact .digital { margin-top: 8px; }
  .footer {
    position: absolute; left: 0; bottom: 0; width: 100%; height: 170px;
    background: var(--band-light);
    padding: 30px 0 0 150px;
    font-family: "Michroma", sans-serif;
    font-variant: small-caps;
    font-size: 15px; letter-spacing: 1.5px;
    color: var(--ink-teal);
  }
  .footer p { margin-bottom: 14px; }
</style>
</head>
<body>
  <div class="letterhead">
    <header class="header">
      <div class="skyline-art" role="img" aria-label="Silhouette of an oil refinery skyline"></div>
      <div class="figure-art" role="img" aria-label="Silhouette of an inspector in a hard hat holding a clipboard"></div>
      <div class="header-rule"></div>
      <h1 class="company-name">Harwell Inspection Services Ltd.</h1>
      <address class="contact">
        <p>Oak House, Mill Lane, Ashcombe,</p>
        <p>Little Brampton</p>
        <p>Wiltshire, SN99 4QX</p>
        <p class="digital">email: office@harwell-inspect.co.uk</p>
        <p>mobile: 07700 900318</p>
      </address>
    </header>
    <footer class="footer">
      <p>Company registration number is:0482615</p>
      <p>Bank Name:</p>
      <p>Account No:</p>
    </footer>
  </div>
</body>
</html>
```